Business Card Design Project

Innovative and Elegant. The firm is an Asset Management Firm that will create a series of Investment Vehicles. Should be Bold but modern. Would like a material that is softer than a traditional Buss Card. Like the logos instead of the words (Telephone, email, fax,etc..)
Look attacked for shape and small telephone logos. Don't like their logo, perhaps took small.
Updates

Have Logo and Buss Card projects running simultaneous so please be coordinated since Logo, of course, will be used in the Buss Card design.

Target Market(s)

High Net Worth Individuals

Industry/Entity Type

Business

Font styles to use
Sans Serif

Requirements
Must have
• Shaped with round corners, like a parking ticket.

```html
<!DOCTYPE html>
<html lang="en">
<head>
<meta charset="utf-8">
<title>Halvern Capital – Business Cards</title>
<link rel="stylesheet" href="https://fonts.googleapis.com/css2?family=Arimo:wght@400;700&display=swap">
<style>
  :root {
    --navy: #1f3f7f;
    --slate: #8a8f93;
    --ink: #1c1c1c;
    --rule: #9a9a9a;
    --paper: #ffffff;
    --mist: #e4e4e4;
    --edge: #d6d6d6;
  }
  * { box-sizing: border-box; margin: 0; padding: 0; }
  html, body { width: 1200px; height: 2192px; overflow: hidden; background: var(--paper); }
  body { position: relative; font-family: "Arimo", Arial, sans-serif; color: var(--ink); }

  .card {
    position: absolute; left: 155px; width: 964px; height: 546px;
    border-radius: 56px; overflow: hidden;
  }
  .abs { position: absolute; white-space: nowrap; line-height: 1; }
  .icon { position: absolute; width: 26px; height: 26px; fill: var(--navy); }

  .holder-name { font-weight: 700; font-size: 37px; color: var(--navy); }
  .holder-role { font-weight: 700; font-size: 28px; color: var(--slate); }
  .contact { font-size: 28px; color: var(--ink); }

  .brand { position: absolute; display: flex; flex-direction: column; align-items: center; }
  .brand-dot { width: 70px; height: 70px; border-radius: 50%; background: var(--navy); margin-bottom: 18px; }
  .brand-name {
    font-weight: 700; font-size: 44px; line-height: 1.1; color: var(--navy);
    text-align: center; letter-spacing: 2px;
  }

  /* Card one */
  .card--soft { top: 126px; background: radial-gradient(ellipse at 30% 50%, #ffffff 0%, #f2f2f2 55%, var(--mist) 100%); }
  .card--soft .rule { position: absolute; left: 81px; top: 336px; width: 401px; height: 2px; background: var(--rule); }

  /* Card two */
  .card--banded { top: 845px; background: var(--paper); }
  .band-top { position: absolute; left: 0; top: 0; width: 100%; height: 48px; background: var(--navy); }
  .band-bottom { position: absolute; left: 0; bottom: 0; width: 100%; height: 96px; background: var(--navy); }
  .divider { position: absolute; left: 446px; top: 17px; width: 4px; height: 417px; background: var(--ink); }
  .band-address { font-size: 34px; color: var(--paper); }
  .band-bottom .icon { fill: var(--paper); width: 36px; height: 36px; }

  /* Card three */
  .card--split { top: 1556px; border: 2px solid var(--edge); background: var(--paper); }
  .split-panel { position: absolute; left: 0; top: 0; width: 446px; height: 100%; background: radial-gradient(ellipse at 50% 40%, #ffffff 0%, #f0f0f0 60%, var(--mist) 100%); }
  .card--split .rule { position: absolute; left: 491px; top: 159px; width: 436px; height: 3px; background: var(--navy); }
</style>
</head>
<body>

<svg width="0" height="0" style="position:absolute" aria-hidden="true">
  <symbol id="i-flag" viewBox="0 0 24 24"><rect x="2" y="3" width="2.4" height="19"/><path d="M4.4 3h15l-3 4.5 3 4.5h-15z"/></symbol>
  <symbol id="i-phone" viewBox="0 0 24 24"><path d="M6.6 2.5l3 3.6-2 2.4c1.4 3 3.9 5.5 6.9 6.9l2.4-2 3.6 3-1.6 3.6C11 20 4 13 2.5 4.1z"/></symbol>
  <symbol id="i-mobile" viewBox="0 0 24 24"><path d="M7 1h10a2 2 0 0 1 2 2v18a2 2 0 0 1-2 2H7a2 2 0 0 1-2-2V3a2 2 0 0 1 2-2zm0 3v9h10V4z"/></symbol>
  <symbol id="i-mail" viewBox="0 0 24 24"><path d="M1 5h22v15H1z"/><path d="M1.5 5.5L12 13l10.5-7.5" fill="none" stroke="#fff" stroke-width="1.6"/></symbol>
  <symbol id="i-web" viewBox="0 0 24 24"><g fill="none" stroke="currentColor" stroke-width="1.8"><circle cx="12" cy="12" r="10"/><ellipse cx="12" cy="12" rx="4.5" ry="10"/><path d="M2 12h20M4 6.5h16M4 17.5h16"/></g></symbol>
  <symbol id="i-building" viewBox="0 0 24 24"><g fill="none" stroke="currentColor" stroke-width="1.6"><path d="M3 2h18v20H3z"/><path d="M6 6h12M6 10h12M6 14h12M6 18h12"/></g></symbol>
</svg>

<!-- Card one: soft grey, brand top right -->
<section class="card card--soft" aria-label="Business card, manager version">
  <div class="brand" style="left:520px; top:28px; width:400px;">
    <div class="brand-dot"></div>
    <div class="brand-name">HALVERN<br>CAPITAL</div>
  </div>
  <div class="abs holder-name" style="left:66px; top:250px;">Tomas Rivera Ortiz</div>
  <div class="abs holder-role" style="left:203px; top:296px;">MANAGER</div>
  <div class="rule"></div>

  <svg class="icon" style="left:37px; top:370px;"><use href="#i-flag"/></svg>
  <div class="abs contact" style="left:87px; top:370px;">Calle Olmos 2280, 4C/C.A.B.A. Argentina</div>

  <svg class="icon" style="left:37px; top:426px;"><use href="#i-phone"/></svg>
  <div class="abs contact" style="left:87px; top:426px;">+54 11 5550-1482</div>
  <svg class="icon" style="left:359px; top:424px;"><use href="#i-mobile"/></svg>
  <div class="abs contact" style="left:406px; top:426px;">+54 911 5550-7309</div>

  <svg class="icon" style="left:37px; top:478px;"><use href="#i-mail"/></svg>
  <div class="abs contact" style="left:93px; top:474px;">tomas@northvale.com</div>
  <svg class="icon" style="left:500px; top:476px; color:var(--navy);"><use href="#i-web"/></svg>
  <div class="abs contact" style="left:558px; top:476px;">www.northvale.com</div>
</section>

<!-- Card two: navy bands, CEO -->
<section class="card card--banded" aria-label="Business card, chief executive version">
  <div class="band-top"></div>
  <div class="brand" style="left:22px; top:150px; width:400px;">
    <div class="brand-dot"></div>
    <div class="brand-name">HALVERN<br>CAPITAL</div>
  </div>
  <div class="divider"></div>

  <div class="abs holder-name" style="left:469px; top:82px;">Tomas Rivera Ortiz</div>
  <div class="abs holder-role" style="left:642px; top:128px;">CEO</div>

  <svg class="icon" style="left:482px; top:212px;"><use href="#i-phone"/></svg>
  <div class="abs contact" style="left:523px; top:212px;">+54 11 5550-1482</div>
  <svg class="icon" style="left:482px; top:273px;"><use href="#i-mobile"/></svg>
  <div class="abs contact" style="left:523px; top:275px;">+54 911 5550-7309</div>
  <svg class="icon" style="left:482px; top:333px;"><use href="#i-mail"/></svg>
  <div class="abs contact" style="left:531px; top:330px;">tomas@northvale.com</div>
  <svg class="icon" style="left:482px; top:387px; color:var(--navy);"><use href="#i-web"/></svg>
  <div class="abs contact" style="left:531px; top:387px;">www.northvale.com</div>

  <div class="band-bottom">
    <svg class="icon" style="left:103px; top:30px; color:var(--paper);"><use href="#i-building"/></svg>
    <div class="abs band-address" style="left:166px; top:31px;">Calle Olmos 2280, 4C/C.A.B.A. - Argentina</div>
  </div>
</section>

<!-- Card three: split panel -->
<section class="card card--split" aria-label="Business card, split layout">
  <div class="split-panel"></div>
  <div class="brand" style="left:22px; top:170px; width:400px;">
    <div class="brand-dot"></div>
    <div class="brand-name">HALVERN<br>CAPITAL</div>
  </div>

  <div class="abs holder-name" style="left:467px; top:70px;">Tomas Rivera Ortiz</div>
  <div class="abs holder-role" style="left:605px; top:114px;">MANAGER</div>
  <div class="rule"></div>

  <svg class="icon" style="left:478px; top:209px;"><use href="#i-flag"/></svg>
  <div class="abs contact" style="left:528px; top:209px; line-height:1.25;">Calle Olmos 2280, 4C/C.A.B.A.<br>Argentina</div>

  <svg class="icon" style="left:478px; top:297px;"><use href="#i-phone"/></svg>
  <div class="abs contact" style="left:528px; top:297px;">+54 11 5550-1482</div>
  <svg class="icon" style="left:478px; top:354px;"><use href="#i-mobile"/></svg>
  <div class="abs contact" style="left:528px; top:356px;">+54 911 5550-7309</div>
  <svg class="icon" style="left:478px; top:412px;"><use href="#i-mail"/></svg>
  <div class="abs contact" style="left:535px; top:409px;">tomas@northvale.com</div>
  <svg class="icon" style="left:478px; top:465px; color:var(--navy);"><use href="#i-web"/></svg>
  <div class="abs contact" style="left:535px; top:465px;">www.northvale.com</div>
</section>

</body>
</html>
```